Business Card Design

We need a business card designed for a new company based in Melbourne called Korvum solutions. Korvum solutions provides management consulting specialising in the health and social services sector.

Korvum solutions offer a unique set of specialist skills │dealing with all levels of government │ unique communication skills│intimate knowledge of the health sector │solutions tailored to unique circumstances.

Korvum solutions takes on a select number of clients at any one time, this ensures that your organisation receives the attention required. On larger projects, Korvum solutions join up with other consultants to bring specialist skills to a project.
Updates

This is the first time I have used Pixel Bazaar and thank you all for responding. The variation is amazing and makes it hard to decide. I have to ask some of my friends to give me their views. The response is fantastic. The one I pick will basically be the most visually appealing

Industry/Entity Type

Management Consulting

Contact Information for Business Card

Marcus Pellow, Principal, Korvum solutions, 14 Wexcombe Ave, Dunlarry VIC 3999, 0400 137 284, marcusp@korvumsolutions.example, www.korvumsolutions.example

```html
<!DOCTYPE html>
<html lang="en">
<head>
<meta charset="utf-8">
<title>Korvum solutions — Business Card</title>
<link rel="stylesheet" href="https://fonts.googleapis.com/css2?family=Didact+Gothic&display=swap">
<style>
  :root {
    --red-edge: #7a1317;
    --red-mid: #a81b22;
    --red-bright: #c9212d;
    --white: #ffffff;
    --ink-grey: #5c5c5c;
    --font-text: "Didact Gothic", sans-serif;
  }
  * { margin: 0; padding: 0; box-sizing: border-box; }
  html, body {
    width: 1200px;
    height: 695px;
    overflow: hidden;
    background: var(--white);
    font-family: var(--font-text);
  }
  .card {
    position: relative;
    width: 1200px;
    height: 695px;
    overflow: hidden;
    background: linear-gradient(90deg, var(--red-edge) 0%, var(--red-mid) 25%, var(--red-bright) 50%, var(--red-mid) 75%, var(--red-edge) 100%);
  }
  .name-band {
    position: absolute;
    left: 0;
    top: 124px;
    width: 1200px;
    height: 196px;
    background: var(--white);
    text-align: center;
    color: var(--ink-grey);
  }
  .person-name {
    position: absolute;
    left: 0;
    right: 0;
    top: 48px;
    font-size: 57px;
    font-weight: 400;
    letter-spacing: 3px;
    line-height: 1;
  }
  .person-role {
    position: absolute;
    left: 0;
    right: 0;
    top: 110px;
    font-size: 30px;
    letter-spacing: 2.5px;
    line-height: 1;
  }
  .company-name {
    position: absolute;
    left: 50px;
    top: 378px;
    font-size: 50px;
    line-height: 1;
    color: var(--white);
    letter-spacing: 1px;
  }
  .contact-list {
    position: absolute;
    left: 48px;
    top: 458px;
    list-style: none;
    color: var(--white);
    font-size: 35px;
    line-height: 1;
  }
  .contact-item {
    display: flex;
    align-items: center;
    height: 48.5px;
  }
  .contact-icon {
    width: 44px;
    height: 34px;
    flex: 0 0 44px;
    margin-right: 6px;
    display: flex;
    align-items: center;
    justify-content: center;
  }
  .contact-icon svg { display: block; fill: var(--white); }
</style>
</head>
<body>
  <div class="card">
    <section class="name-band">
      <h1 class="person-name">Marcus Pellow</h1>
      <p class="person-role">(Principal)</p>
    </section>

    <div class="company-name">Korvum solutions</div>

    <ul class="contact-list">
      <li class="contact-item">
        <span class="contact-icon">
          <svg width="18" height="26" viewBox="0 0 18 26" aria-hidden="true">
            <path d="M9 0C4 0 0 4 0 9c0 6.5 9 17 9 17s9-10.5 9-17C18 4 14 0 9 0zm0 12.5A3.5 3.5 0 1 1 9 5.5a3.5 3.5 0 0 1 0 7z"/>
          </svg>
        </span>
        <span class="contact-text">14 Wexcombe Ave, Dunlarry VIC 3999</span>
      </li>
      <li class="contact-item">
        <span class="contact-icon">
          <svg width="30" height="26" viewBox="0 0 30 26" aria-hidden="true">
            <path d="M15 2C8 2 1 3.5 1 7.5V11h7V7.5c2-.8 4.5-1 7-1s5 .2 7 1V11h7V7.5C29 3.5 22 2 15 2z"/>
            <path d="M9 11l-4 7v7h20v-7l-4-7h-3v2h-6v-2H9zm6 4a3.5 3.5 0 1 1 0 7 3.5 3.5 0 0 1 0-7z"/>
          </svg>
        </span>
        <span class="contact-text">0400 137 284</span>
      </li>
      <li class="contact-item">
        <span class="contact-icon">
          <svg width="40" height="26" viewBox="0 0 40 26" aria-hidden="true">
            <path d="M0 0h40v26H0z M3 3l17 13L37 3v3L20 19 3 6z" fill-rule="evenodd"/>
          </svg>
        </span>
        <span class="contact-text">marcusp@korvumsolutions.example</span>
      </li>
      <li class="contact-item">
        <span class="contact-icon">
          <svg width="28" height="28" viewBox="0 0 28 28" aria-hidden="true" fill="none" stroke="#ffffff" stroke-width="2">
            <circle cx="14" cy="14" r="12"/>
            <ellipse cx="14" cy="14" rx="5.5" ry="12"/>
            <line x1="2" y1="14" x2="26" y2="14"/>
            <path d="M4 8h20M4 20h20"/>
          </svg>
        </span>
        <span class="contact-text">www.korvumsolutions.example</span>
      </li>
    </ul>
  </div>
</body>
</html>
```